Athletic Director Business Card

I need a business card that is very appealing and shows my school logo and colours (red, white and black). We just finished changing our school logo and have sent the two logos we use and I have also sent the logo W that we also use. I'm not sure if combining them works but I thought I would send it anyway and let your creative juices flow. Looking for a simple but very luring design. It could have the different sports on it but I think doing something with the logo is probably the direction I would like to see as we offer 11 different sports and 22 different teams so that might get to busy. We have a long "Tradition of Excellence" and maybe that could be on the card. If you need to change to logo by shadowing it, or making it a two colour with a glow in it or what every you think would make it look fantastic give it a try as I'm open to different looks.

Target Market(s)

Parents of high school athletes, businesses throughout our city, principals.

Industry/Entity Type

School

Requirements
Must have
• Name of School - Ridgemont Valley High School or just Ridgemont Valley.
My Name - Marcus Holloway
Position - Athletic Director
Phone - 403-555-0147
Cell - 403-555-0183
Email - mkholloway@pvsd.ab.ca
Website - www.ridgemontvalleyathletics.com

```html
<!DOCTYPE html>
<html lang="en">
<head>
<meta charset="utf-8">
<title>Ridgemont Valley Athletics – Business Card</title>
<link rel="stylesheet" href="https://fonts.googleapis.com/css2?family=Lato:wght@400;700&display=swap">
<style>
  :root {
    --ink: #0d0d0d;
    --ink-soft: #2a2a2a;
    --paper: #f4f4f4;
    --red: #e3232f;
    --grey-text: #5a5a5a;
    --stage: #e9e6e1;
  }
  * { margin: 0; padding: 0; box-sizing: border-box; }
  html, body {
    width: 1200px; height: 1023px; overflow: hidden;
    background: var(--stage);
    font-family: "Lato", Arial, sans-serif;
  }
  .canvas { position: relative; width: 1200px; height: 1023px; }

  .card {
    position: absolute; width: 700px; height: 400px;
    border-radius: 6px; overflow: hidden;
    box-shadow: 0 18px 40px rgba(0,0,0,.28);
  }
  .card-front { left: 90px; top: 80px; }
  .card-back { left: 410px; top: 540px; }
  .card-art { position: absolute; inset: 0; }

  /* Front */
  .school-mark {
    position: absolute; left: 70px; top: 178px;
    display: flex; align-items: center; gap: 16px;
  }
  .school-mark .square { width: 34px; height: 34px; background: var(--red); }
  .school-name { color: #fff; font-weight: 700; font-size: 24px; letter-spacing: .2px; }

  .contact {
    position: absolute; right: 30px; top: 100px; width: 260px; text-align: right;
  }
  .person-name { color: var(--grey-text); font-size: 23px; font-weight: 400; letter-spacing: .3px; }
  .person-role { color: var(--grey-text); font-size: 15px; margin-top: 2px; padding-right: 14px; }
  .rule {
    height: 3px; background: var(--ink-soft); width: 160px;
    margin: 18px 14px 18px auto;
  }
  .contact-list { list-style: none; }
  .contact-list li {
    display: flex; justify-content: flex-end; align-items: center; gap: 10px;
    color: var(--red); font-size: 16px; height: 28px;
  }
  .icon {
    width: 20px; height: 20px; background: var(--ink-soft); border-radius: 2px;
    display: inline-flex; align-items: center; justify-content: center; flex: none;
  }
  .website {
    position: absolute; right: 30px; bottom: 30px;
    display: flex; align-items: center; gap: 10px;
    color: var(--red); font-size: 15px;
  }

  /* Back */
  .team-mark {
    position: absolute; left: 250px; top: 110px;
    display: flex; align-items: center; gap: 18px;
  }
  .team-mark .circle { width: 54px; height: 54px; border-radius: 50%; background: var(--red); }
  .team-name { color: #fff; font-weight: 700; font-size: 38px; letter-spacing: .5px; }
  .tagline {
    position: absolute; left: 58px; top: 52px;
    transform-origin: left top; transform: rotate(90deg) translateY(-100%);
    color: #fff; font-size: 28px; white-space: nowrap; letter-spacing: .3px;
  }
</style>
</head>
<body>
<main class="canvas">

  <section class="card card-front" aria-label="Business card front">
    <svg class="card-art" viewBox="0 0 700 400" width="700" height="400" aria-hidden="true">
      <defs>
        <linearGradient id="gloss" x1="0" y1="0" x2="1" y2="1">
          <stop offset="0" stop-color="#2b2b2b"/>
          <stop offset=".45" stop-color="#0d0d0d"/>
          <stop offset="1" stop-color="#000"/>
        </linearGradient>
      </defs>
      <rect width="700" height="400" fill="url(#gloss)"/>
      <polygon class="zig-band" points="538,0 560,0 548,55 528,40 355,400 332,400 508,28 527,44" fill="#e3232f"/>
      <polygon class="paper-side" points="560,0 700,0 700,400 355,400 528,40 548,55" fill="#f4f4f4"/>
    </svg>

    <div class="school-mark">
      <span class="square"></span>
      <span class="school-name">Ridgemont Valley</span>
    </div>

    <div class="contact">
      <p class="person-name">Marcus Holloway</p>
      <p class="person-role">Athletic Director</p>
      <div class="rule"></div>
      <ul class="contact-list">
        <li>403-555-0147
          <span class="icon"><svg width="12" height="12" viewBox="0 0 12 12"><path d="M2 1h2.5l1 2.6-1.4 1a6 6 0 0 0 3.3 3.3l1-1.4L11 7.5V10a1 1 0 0 1-1 1A9 9 0 0 1 1 2a1 1 0 0 1 1-1z" fill="#fff"/></svg></span>
        </li>
        <li>403-555-0183
          <span class="icon"><svg width="12" height="12" viewBox="0 0 12 12"><rect x="3" y=".5" width="6" height="11" rx="1" fill="none" stroke="#fff" stroke-width="1.2"/><circle cx="6" cy="9.5" r=".7" fill="#fff"/></svg></span>
        </li>
        <li>mkholloway@pvsd.ab.ca
          <span class="icon"><svg width="13" height="12" viewBox="0 0 13 12"><rect x="1" y="2.5" width="11" height="7" fill="none" stroke="#fff" stroke-width="1.1"/><path d="M1 2.5l5.5 4 5.5-4" fill="none" stroke="#fff" stroke-width="1.1"/></svg></span>
        </li>
      </ul>
    </div>
    <p class="website">www.ridgemontvalleyathletics.com
      <span class="icon"><svg width="12" height="12" viewBox="0 0 12 12"><circle cx="6" cy="6" r="5" fill="none" stroke="#fff" stroke-width="1.1"/><ellipse cx="6" cy="6" rx="2.2" ry="5" fill="none" stroke="#fff" stroke-width="1"/><path d="M1 6h10" stroke="#fff" stroke-width="1"/></svg></span>
    </p>
  </section>

  <section class="card card-back" aria-label="Business card back">
    <svg class="card-art" viewBox="0 0 700 400" width="700" height="400" aria-hidden="true">
      <defs>
        <linearGradient id="gloss-back" x1="0" y1="0" x2="1" y2="1">
          <stop offset="0" stop-color="#262626"/>
          <stop offset=".5" stop-color="#0d0d0d"/>
          <stop offset="1" stop-color="#000"/>
        </linearGradient>
      </defs>
      <rect width="700" height="400" fill="url(#gloss-back)"/>
    </svg>
    <p class="tagline">Tradition of Excellence</p>
    <div class="team-mark">
      <span class="circle"></span>
      <span class="team-name">Ridge Runners</span>
    </div>
  </section>

</main>
</body>
</html>
```